Lantern Ridge Treks Flyer

I have an adventure travel company and I need a flyer to promote my trip to Ukraine.
I would like to have a universal flyer that I can change based on the trip.
The Title should say "Travel to Ukraine: 9 Day Eastern European Adventure"
The date should be under the title.
The background photo should be kiev2.jpg
The highlights of the trip, then price $1200 and what it includes. See the text for highlights and includes sections here:
http://www.lanternridgetreks.com/#!featured-trip
The website link (www.lanternridgetreks.com) should be somewhere in the bottom.
You can use other photos provided or from my website that relates to Ukraine trip.
Travel

```html
<!DOCTYPE html>
<html lang="en">
<head>
<meta charset="utf-8">
<title>Travel to Ukraine – Lantern Ridge Treks</title>
<link rel="stylesheet" href="https://fonts.googleapis.com/css2?family=Archivo+Black&display=swap">
<style>
  :root {
    --teal: #2f8aa0;
    --yellow: #f3dc2c;
    --ink: #0d0d0d;
    --paper: #ffffff;
    --halo: #8a8a8a;
    --star: #c9e04a;
    --price: #2c5bb3;
  }
  * { box-sizing: border-box; margin: 0; padding: 0; }
  html, body { width: 848px; height: 1200px; overflow: hidden; background: #ffffff; }
  .flyer {
    position: relative; width: 848px; height: 1200px; overflow: hidden;
    font-family: "Archivo Black", "Arial Black", sans-serif; color: var(--ink);
    background: linear-gradient(90deg, var(--teal) 0 50.5%, var(--yellow) 50.5% 100%);
  }
  .flyer::before {
    content: ""; position: absolute; inset: 0;
    background:
      radial-gradient(ellipse at 10% 70%, rgba(0,40,60,.25), transparent 45%),
      radial-gradient(ellipse at 90% 20%, rgba(200,150,0,.18), transparent 40%),
      radial-gradient(ellipse at 80% 85%, rgba(200,150,0,.15), transparent 40%);
  }
  .abs { position: absolute; }

  .title { left: 0; width: 100%; text-align: center; color: var(--paper); white-space: nowrap;
    text-shadow: 0 0 6px var(--halo), 0 0 10px var(--halo), 0 0 14px #555; }
  .title-1 { top: 30px; font-size: 40px; }
  .title-2 { top: 82px; font-size: 42px; letter-spacing: -0.5px; }

  .tag { display: inline-block; background: var(--ink); color: var(--paper); padding: 2px 10px; line-height: 1.1; white-space: nowrap; }
  .date { left: 40px; top: 182px; width: 370px; transform: rotate(-8deg); text-align: center; }
  .date-label { font-size: 38px; }
  .date-range { font-size: 25px; margin-top: 2px; padding: 3px 10px; }

  .starburst { left: 71px; top: 285px; width: 292px; height: 190px; transform: rotate(-6deg); }
  .price { left: 140px; top: 356px; font-size: 40px; color: var(--price); transform: rotate(-5deg); }

  .included-label { left: 372px; top: 258px; transform: rotate(-8deg); font-size: 40px; padding: 0 12px; }
  .dot { width: 14px; height: 14px; border-radius: 50%; background: var(--ink); }

  .item { font-size: 25px; line-height: 32px; height: 32px; white-space: nowrap; transform-origin: left center; }
  .item.bullet { padding-left: 22px; }
  .item.bullet::before { content: ""; position: absolute; left: 0; top: 9px; width: 15px; height: 15px; border-radius: 50%; background: var(--ink); }
  .item-nights { left: 437px; top: 338px; transform: rotate(-6deg); }
  .item-meals { left: 341px; top: 378px; transform: rotate(4deg); }
  .item-guides { left: 402px; top: 421px; transform: rotate(4deg); }
  .item-transport { left: 527px; top: 468px; transform: rotate(9deg); }
  .item-destination { left: 556px; top: 514px; transform: rotate(7deg); }
  .item-leader { left: 541px; top: 548px; transform: rotate(20deg); }
  .item-times { left: 549px; top: 600px; transform: rotate(22deg); }

  .photo { background: var(--paper); padding: 12px; box-shadow: 2px 3px 6px rgba(0,0,0,.35); }
  .photo-fill { width: 100%; height: 100%; }
  .photo-tram { left: 42px; top: 484px; width: 458px; height: 300px; transform: rotate(-1deg); }
  .photo-tram .photo-fill { background: linear-gradient(160deg, #c7c4b3 0%, #b5ab8f 40%, #a9432f 62%, #8c8a7a 80%, #6f6d62 100%); }
  .photo-cave { left: 315px; top: 664px; width: 254px; height: 196px; transform: rotate(-9deg); }
  .photo-cave .photo-fill { background: radial-gradient(ellipse at 50% 50%, #b08a60 0%, #7a5634 50%, #3f2a1a 100%); }
  .photo-church { left: 376px; top: 782px; width: 450px; height: 334px; transform: rotate(4deg); }
  .photo-church .photo-fill { background: linear-gradient(180deg, #9fb0c0 0%, #8e9a88 30%, #d0a640 55%, #6f5a3f 80%, #4c4536 100%); }

  .plus { left: 717px; top: 702px; width: 86px; height: 86px; }
  .dashes { left: 0; top: 0; width: 848px; height: 1200px; }

  .all-label { left: 138px; top: 846px; transform: rotate(8deg); font-size: 40px; padding: 0 12px; }
  .all-list { left: 12px; top: 890px; width: 420px; list-style: none; transform: rotate(8deg); transform-origin: left top; }
  .all-list li { font-size: 24px; line-height: 1.35; position: relative; padding-left: 24px; white-space: nowrap; }
  .all-list li::before { content: ""; position: absolute; left: 0; top: 10px; width: 14px; height: 14px; border-radius: 50%; background: var(--ink); }

  .site { left: 0; width: 100%; top: 1126px; text-align: center; }
  .site-link { display: inline-block; background: var(--ink); color: var(--paper); font-size: 42px; line-height: 1.1; padding: 6px 26px 8px; border-radius: 40px; text-decoration: none; }
</style>
</head>
<body>
<main class="flyer">
  <h1 class="abs title title-1">Travel to Ukraine:</h1>
  <h2 class="abs title title-2">9 Day Eastern European Adventure</h2>

  <svg class="abs starburst" viewBox="0 0 300 200" aria-hidden="true">
    <polygon fill="var(--star)" points="150,0 178,62 262,30 218,92 300,112 212,128 236,198 160,150 96,200 100,136 0,148 76,104 22,52 108,70"/>
  </svg>
  <div class="abs price">$1,200</div>

  <div class="abs date">
    <div class="tag date-label">DATE:</div><br>
    <div class="tag date-range">Fri May 18 - Sun May 27</div>
  </div>

  <div class="abs tag included-label">Included</div>
  <span class="abs dot" style="left:592px;top:258px"></span>
  <span class="abs dot" style="left:600px;top:292px"></span>

  <div class="abs item bullet item-nights">9 nights acommodations</div>
  <div class="abs item bullet item-meals">Breakfast, lunch &amp; dinner daily</div>
  <div class="abs item bullet item-guides">English speaking tour guides</div>
  <div class="abs item item-transport">&amp; transportation at</div>
  <div class="abs item item-destination">every destination</div>
  <div class="abs item bullet item-leader">Tour leader from USA</div>
  <div class="abs item item-times">at ALL TIMES</div>

  <svg class="abs dashes" viewBox="0 0 848 1200" aria-hidden="true">
    <line x1="572" y1="756" x2="700" y2="730" stroke="var(--ink)" stroke-width="12" stroke-dasharray="14 12"/>
    <line x1="246" y1="858" x2="330" y2="806" stroke="var(--ink)" stroke-width="12" stroke-dasharray="14 12"/>
  </svg>

  <div class="abs photo photo-tram"><div class="photo-fill" role="img" aria-label="Photo of a red tram on a tree-lined city street"></div></div>
  <div class="abs photo photo-church"><div class="photo-fill" role="img" aria-label="Aerial photo of a monastery with golden domes above a river"></div></div>
  <div class="abs photo photo-cave"><div class="photo-fill" role="img" aria-label="Photo of a cave interior with rock formations"></div></div>

  <svg class="abs plus" viewBox="0 0 86 86" aria-hidden="true">
    <rect x="33" y="0" width="20" height="86" fill="var(--ink)"/>
    <rect x="0" y="33" width="86" height="20" fill="var(--ink)"/>
  </svg>

  <div class="abs tag all-label">ALL</div>
  <ul class="abs all-list">
    <li>Group transfers (Trains,<br>buses,and vans),<br>Sightseeing tours and<br>entrance fees</li>
  </ul>

  <div class="abs site"><a class="site-link" href="http://www.lanternridgetreks.com/#!featured-trip">www.lanternridgetreks.com</a></div>
</main>
</body>
</html>
```